Redesign business card for Wade Linford Construction

Basically I want a complete redesign of the business card I have attached with this project. The only stipulations I have are that the colors , crimson and white, stay the same and all of the information on the old card is also on the new design. Also I would like to add that we also specialize in metal building foundations as well. I look forward to seeing what you all come up with.
Industry/Entity Type
Business
Contact Information for Business Card
All of the details are on the attachment I have included with this project
Look and feel
Each slider illustrates characteristics of the customer's brand and the style your logo design should communicate.

```html
<!DOCTYPE html>
<html lang="en">
<head>
<meta charset="utf-8">
<title>Wade Linford Construction – Business Card</title>
<link rel="stylesheet" href="https://fonts.googleapis.com/css2?family=Lato:wght@400;700&display=swap">
<style>
  :root {
    --crimson: #dc2430;
    --crimson-deep: #c81c27;
    --white: #ffffff;
    --paper: #fbfbfb;
    --backdrop: #e7e7e7;
    --faint-line: rgba(255, 215, 205, 0.45);
  }
  * { margin: 0; padding: 0; box-sizing: border-box; }
  html, body {
    width: 1200px; height: 720px; overflow: hidden;
    background: var(--backdrop);
    font-family: "Lato", sans-serif;
  }
  .canvas { position: relative; width: 1200px; height: 720px; }

  .card {
    position: absolute; top: 241px;
    width: 419px; height: 239px;
    border-radius: 14px; overflow: hidden;
  }
  .card--front { left: 148px; background: var(--paper); }
  .card--back {
    left: 633px;
    background: linear-gradient(135deg, var(--crimson), var(--crimson-deep));
    color: var(--white); text-align: center;
  }

  .front-sweep { position: absolute; inset: 0; width: 419px; height: 239px; }

  .brand-mark { position: absolute; left: 17px; top: 16px; width: 80px; height: 80px; }
  .brand-heading {
    position: absolute; left: 107px; top: 33px;
    color: var(--crimson); font-weight: 700; line-height: 1.2;
  }
  .brand-name { font-size: 15px; margin-bottom: 4px; }
  .brand-service { font-size: 12px; line-height: 17px; }

  .address {
    position: absolute; left: 26px; top: 144px;
    color: var(--crimson); font-size: 12px; line-height: 16px;
  }

  .person {
    position: absolute; right: 10px; top: 105px;
    color: var(--white); text-align: right;
  }
  .person-name { font-size: 14px; font-weight: 700; line-height: 18px; }
  .person-role, .person-nickname { font-size: 11.5px; line-height: 16px; }

  .contacts {
    position: absolute; right: 10px; top: 167px;
    list-style: none; color: var(--white);
    font-size: 11px; line-height: 15px; text-align: right;
  }
  .contacts li { display: flex; justify-content: flex-end; align-items: center; gap: 4px; }
  .contacts b { font-weight: 700; }
  .contacts svg { width: 10px; height: 10px; fill: var(--white); flex: none; }

  .back-mark { position: absolute; left: 122px; top: 4px; width: 230px; height: 230px; }
  .back-name {
    position: relative; margin-top: 68px;
    font-size: 19px; font-weight: 700;
  }
  .back-specialty {
    position: relative; width: 380px; margin: 18px auto 0;
    font-size: 13.5px; line-height: 19px;
  }
</style>
</head>
<body>
<main class="canvas">

  <section class="card card--front" aria-label="Business card front">
    <svg class="front-sweep" viewBox="0 0 419 239" aria-hidden="true">
      <defs>
        <linearGradient id="sweepFill" x1="0" y1="0" x2="1" y2="1">
          <stop offset="0" stop-color="#e02a36"/>
          <stop offset="1" stop-color="#cd1e29"/>
        </linearGradient>
      </defs>
      <path d="M378 0 H419 V239 H8 C150 205 300 120 378 0 Z" fill="url(#sweepFill)"/>
    </svg>

    <svg class="brand-mark" viewBox="0 0 80 80" aria-hidden="true">
      <circle cx="40" cy="40" r="37" fill="none" stroke="var(--crimson)" stroke-width="4"/>
    </svg>

    <div class="brand-heading">
      <p class="brand-name">Wade Linford Construction</p>
      <p class="brand-service">Concrete Contractor</p>
      <p class="brand-service">Metal Building Foundations</p>
    </div>

    <address class="address" style="font-style:normal">
      118 Birch Hollow Rd.<br>Millbrook Falls, AL 36099
    </address>

    <div class="person">
      <p class="person-name">Wade Linford</p>
      <p class="person-role">Owner/Founder</p>
      <p class="person-nickname">"ROCKSOLID"</p>
    </div>

    <ul class="contacts">
      <li><span><b>Business:</b> 555.201.4830</span>
        <svg viewBox="0 0 10 10"><path d="M1 3 Q5 0 9 3 L8 4.5 L6.5 3.8 V3 H3.5 V3.8 L2 4.5 Z M2.5 5 H7.5 L8.5 9 H1.5 Z"/></svg></li>
      <li><span><b>Mobile:</b> 555.201.4831</span>
        <svg viewBox="0 0 10 10"><path d="M2.5 0.5 H7.5 V9.5 H2.5 Z M3.3 1.5 V7.8 H6.7 V1.5 Z"/></svg></li>
      <li><span><b>Home:</b> 555.318.2904</span>
        <svg viewBox="0 0 10 10"><path d="M0.5 0.5 H9.5 V9.5 H0.5 Z M3 2 Q2 5 5.5 8 L7 7 L6 5.8 L5.3 6.3 Q4 5 4 3.6 L4.6 3 L3.8 2 Z" fill-rule="evenodd"/></svg></li>
      <li><span>wlconstruction1992@example.com</span>
        <svg viewBox="0 0 10 10"><path d="M0.5 2 H9.5 V8 H0.5 Z M1.2 2.6 L5 5.6 L8.8 2.6" fill-rule="evenodd"/></svg></li>
    </ul>
  </section>

  <section class="card card--back" aria-label="Business card back">
    <svg class="back-mark" viewBox="0 0 230 230" aria-hidden="true">
      <circle cx="115" cy="115" r="112" fill="none" stroke="var(--faint-line)" stroke-width="1.5"/>
    </svg>
    <h1 class="back-name">Wade Linford</h1>
    <p class="back-specialty">Specialaizing in concrete foundaations, driveways, storm rooms,additons, and most other forms of concreat work.</p>
  </section>

</main>
</body>
</html>
```